Protein Powder Product Label Design

We are going to launch Protein Powder Product shortly and looking for the Unique, Attractive and Best Product label Design. The label size should be 5.5x17.

Here are some competitors label design which I like the most:
https://trelquo.com/collections/daily-nutrition/products/dorn-pax-organic?variant=48201937561420 (Like the way it described each nutrition element at the bottom & Flavors Image)
https://www.quimbrix.com/products/calmrise-stress-anxiety-relief (Like the Logo on Side)
www.7xq.ord (Overall Designs & Color Combination)

I have attached Generic Product Label design template so that you can have all the content required for the label.

Target Market(s)

Nutrition, Sport Nutrition, Protein Powder

Industry/Entity Type

Nutrition

Font styles to use
Sans Serif

Requirements
Must have
• 1. Follows proper Label Guidelines
2. Within Given Label Dimensions
3. Attractive & Unique Label Designs
4. Excellent Color Combinations
Nice to have
• My Product containers will a Black Color Tub. Adjust the label background color accordingly so that it looks attractive.
Should not have
• Exact Label designs for any existing products

```html
<!DOCTYPE html>
<html lang="en">
<head>
<meta charset="utf-8">
<title>Vegan Protein Powder – Chocolate Milkshake Label</title>
<link rel="stylesheet" href="https://fonts.googleapis.com/css2?family=Oswald:wght@500;600&family=Montserrat:wght@400;500&family=Open+Sans:wght@400;600;700&display=swap">
<style>
:root{
  --page:#f1f1f3;
  --label:#e3e5e8;
  --ink:#2b2b2b;
  --muted:#555a5e;
  --brand:#74a9bb;
  --band:#9ccbdb;
  --band-ink:#3f6f80;
  --rule:#3a3a3a;
  --choc:#5a2e1c;
  --choc-light:#8a4f33;
  --gold:#c9a862;
}
*{box-sizing:border-box;margin:0;padding:0}
html,body{width:1200px;height:799px;overflow:hidden;background:var(--page)}
body{font-family:"Open Sans",sans-serif;color:var(--ink)}
.label{
  position:absolute;left:20px;top:170px;width:1160px;height:460px;
  background:var(--label);display:grid;grid-template-columns:370px 420px 370px;
  box-shadow:0 2px 10px rgba(0,0,0,.08);
}
.panel{position:relative;height:100%}
.band{position:absolute;left:0;right:0;bottom:30px;height:28px;background:var(--band)}

/* left panel */
.panel--info{padding:24px 26px 0 34px;font-size:8.4px;line-height:1.45;color:var(--muted)}
.panel--info p{margin-bottom:10px}
.amino{border:1px solid var(--rule);margin-top:4px;font-size:7.4px}
.amino__head{text-align:center;border-bottom:1px solid var(--rule);padding:3px 0 2px;line-height:1.2}
.amino__head small{display:block;font-size:5.5px}
.amino__grid{display:grid;grid-template-columns:1fr 1fr;column-gap:12px;padding:3px 4px;border-bottom:1px solid var(--rule)}
.amino__grid span{display:flex;justify-content:space-between;line-height:1.5}
.amino__total{padding:2px 4px}
.usage{border:1px solid var(--rule);margin-top:12px;padding:4px 5px;font-size:9px;line-height:1.35}
.disclaimer{position:absolute;left:34px;right:26px;bottom:31px;height:26px;border:1px solid var(--rule);border-top:none;font-size:5.2px;line-height:1.3;padding:2px 4px;color:var(--ink);z-index:1}

/* front panel */
.panel--front{text-align:center}
.front__title{font-family:"Oswald",sans-serif;font-weight:500;color:var(--brand);font-size:96px;letter-spacing:22px;line-height:1;margin:24px 0 0 22px}
.front__sub{display:inline-block;background:var(--brand);color:#fff;font-family:"Oswald",sans-serif;font-weight:600;font-size:27px;letter-spacing:2px;padding:0 8px;margin-top:8px;line-height:38px;word-spacing:10px}
.front__art{position:absolute;left:120px;top:172px;width:200px;height:150px;border-radius:40% 55% 45% 50%;background:radial-gradient(circle at 45% 40%,var(--choc-light),var(--choc) 70%)}
.front__seal{position:absolute;left:58px;top:268px;width:64px;height:64px;border-radius:50%;background:radial-gradient(circle,#efe3c4,var(--gold))}
.front__flavor{position:absolute;left:0;right:0;top:332px;font-family:"Montserrat",sans-serif;font-size:14.5px;letter-spacing:1px;line-height:1.35}
.front__net{position:absolute;left:0;right:0;bottom:30px;height:28px;line-height:28px;font-family:"Montserrat",sans-serif;font-size:12.5px;letter-spacing:1.5px;color:var(--band-ink);z-index:1;word-spacing:4px}

/* right panel */
.badges{position:absolute;left:22px;top:28px;display:flex;flex-direction:column;gap:14px}
.badge{width:28px;height:28px;border-radius:50%;border:2px solid var(--ink);background:#fff}
.badge--square{border-radius:2px;height:18px}
.facts{position:absolute;left:92px;top:18px;width:256px;border:1px solid var(--rule);padding:2px 4px;font-size:7px;line-height:1.45}
.facts h2{font-family:"Open Sans",sans-serif;font-weight:400;font-size:15px;line-height:1.1}
.facts__thick{border-top:4px solid var(--rule);margin:2px 0}
.facts__row{display:flex;justify-content:space-between;border-bottom:1px solid #9a9a9a}
.facts__row--ind{padding-left:6px}
.facts__row--sub{padding-left:10px}
.facts__note{font-size:5.5px;line-height:1.3}
.other{position:absolute;left:92px;top:340px;width:256px;font-size:5.6px;line-height:1.3}
.maker{position:absolute;left:92px;bottom:31px;height:26px;font-size:5.2px;line-height:1.25;color:var(--ink);z-index:1}
</style>
</head>
<body>
<main class="label">

  <section class="panel panel--info">
    <p>If you are looking for a healthier alternative to animal-based protein you have found it! Vegan protein is made up of three vegan proteins; Quinoa, Brown Rice and Pea Isolate. These provide amino acids, vitamins, and the minerals that your body needs. They are also higher in fiber which will aid in weight management.</p>
    <p>Vegan Protein contains no artificial sweeteners, colors or flavors. This, along with the protein blend, will help relieve stress on your digestive system. A blend of eleven different super fruits provides antioxidants to help you with your overall health.</p>
    <div class="amino">
      <div class="amino__head">Approximate Amino Acids &nbsp;&nbsp; per Serving<small>(Naturally Occurring)</small></div>
      <div class="amino__grid">
        <span>Alanine <b>850 mg</b></span><span>Arginine <b>1565 mg</b></span>
        <span>Aspartic Acid <b>2180 mg</b></span><span>Cystine <b>184 mg</b></span>
        <span>Glutamic Acid <b>3240 mg</b></span><span>Glycine <b>3127 mg</b></span>
        <span>Histidine <b>501 mg</b></span><span>Isoleucine* <b>929 mg</b></span>
        <span>Leucine* <b>1670 mg</b></span><span>Lysine <b>1403 mg</b></span>
        <span>Methionine <b>189 mg</b></span><span>Phenylalanine <b>1055 mg</b></span>
        <span>Proline <b>898 mg</b></span><span>Serine <b>900 mg</b></span>
        <span>Threonine <b>709 mg</b></span><span>Tryptophan <b>157 mg</b></span>
        <span>Tyrosine <b>676 mg</b></span><span>Valine* <b>1030 mg</b></span>
      </div>
      <div class="amino__total">Total BCAAs .. 3629 mg</div>
    </div>
    <div class="usage">Suggested Use: Mix one heaping scoop with 4-6oz of water, milk, or your favorite beverage. Vary the amount of liquid for taste preference.</div>
    <div class="disclaimer">* These statements have not been evaluated by the Food and Drug Administration. This product is not intended to diagnose, treat, cure or prevent any disease.</div>
    <div class="band"></div>
  </section>

  <section class="panel panel--front">
    <h1 class="front__title">VEGAN</h1>
    <div class="front__sub">PROTEIN POWDER</div>
    <div class="front__art" role="img" aria-label="Chocolate pieces splashing in melted chocolate"></div>
    <div class="front__seal" role="img" aria-label="Gold satisfaction guaranteed seal"></div>
    <div class="front__flavor">Chococlate Milkshake<br>Natural Flavor</div>
    <div class="band"></div>
    <div class="front__net">NET WT. 907G (2 LB) DIETARY SUPPLEMENT</div>
  </section>

  <section class="panel panel--facts">
    <div class="badges">
      <div class="badge" role="img" aria-label="Non-GMO badge"></div>
      <div class="badge" role="img" aria-label="Gluten free badge"></div>
      <div class="badge" role="img" aria-label="GMP certified badge"></div>
      <div class="badge" role="img" aria-label="Made in USA badge"></div>
      <div class="badge" role="img" aria-label="Recycle badge"></div>
      <div class="badge" role="img" aria-label="Vegan product badge"></div>
      <div class="badge badge--square" role="img" aria-label="Regulatory badge"></div>
    </div>
    <div class="facts">
      <h2>Supplement Facts</h2>
      <div>Serving Size 32g</div>
      <div>Servings Per Container 28</div>
      <div class="facts__thick"></div>
      <div class="facts__row"><span>Amount Per Serving</span><span>% Daily Value**</span></div>
      <div class="facts__row"><span>Calories 140</span><span></span></div>
      <div class="facts__row"><span>Total Fat 3 g</span><span>4%</span></div>
      <div class="facts__row facts__row--ind"><span>Saturated Fat 1 g</span><span>5%</span></div>
      <div class="facts__row"><span>Sodium 310 mg</span><span>14%</span></div>
      <div class="facts__row"><span>Total Carbohydrate 6 g</span><span>2%</span></div>
      <div class="facts__row facts__row--ind"><span>Dietary Fiber 2 g</span><span>7%</span></div>
      <div class="facts__row facts__row--ind"><span>Total Sugars 2 g</span><span></span></div>
      <div class="facts__row facts__row--sub"><span>Includes 2g Added Sugars</span><span>4%</span></div>
      <div class="facts__row"><span>Protein 20 g</span><span>41%</span></div>
      <div class="facts__row"><span>Vitamin D 0 mcg</span><span>0%</span></div>
      <div class="facts__row"><span>Calcium 34 mg</span><span>2%</span></div>
      <div class="facts__row"><span>Iron 6 mg</span><span>35%</span></div>
      <div class="facts__row"><span>Potassium 57 mg</span><span>2%</span></div>
      <div class="facts__thick"></div>
      <div class="facts__row"><span>Vegan Protein Blend 25 g<br>&nbsp;(Pea Protein Isolate, Brown Rice Protein, Quinoa)</span><span>‡</span></div>
      <div class="facts__row"><span>MCT Oil Powder 400 mg<br>&nbsp;(Natural MCT Oil, Maltodextrin, Modified Food Starch)</span><span>‡</span></div>
      <div class="facts__row"><span>Antioxidant Blend 150mg<br>&nbsp;(Acai Berry, Acerola, Amla, Jabuticaba, Cranberry,<br>&nbsp;Goji, Mangosteen, Maqui Berry, Pomegranate,<br>&nbsp;Strawberry, Organic Schisandra)</span><span>‡</span></div>
      <div class="facts__note">**Percent Daily Values are based on a 2,000 calorie diet.<br>‡Daily Value not established.</div>
    </div>
    <div class="other">Other Ingredients: Creamer (High Oleic Sunflower Oil, Tapioca Starch, Tapioca Dextrin, Natural Flavors, D-Alpha Tocopherols), Raw Sugar, Natural Flavors, Cocoa (processed with alkali), Stevia, Xanthan Gum.</div>
    <div class="maker">Manufactured for<br>COMPANY<br>Address<br>City, State, Zip</div>
    <div class="band"></div>
  </section>

</main>
</body>
</html>
```